Homepage layout for online ad network

Attached is our Valtry Media logo and updated brief (I can't seem to delete the old logo and brief, but they're no longer relevant).

This project was originally posted with a different logo and corporate name, but we have decided to stay with our current logo and name and redesign the site.

Your design is for a homepage only - design, no coding (I'll get someone else to take your PSD and code it).

Your homepage will make use of a Flash slider - BUT YOU ARE NOT REQUIRED TO PROVIDE THE FLASH. Instead, simply provide the layout and at least two static examples out of the four different sections that will eventually be in the slider.

Much of this design is based on the design of a competitor (listed in the brief).

Please ask whatever questions you need to in order to clarify instructions.
Updates

Project updated to include new logo (and correspondingly new color scheme).

Brief changed slightly.

Thank you for submitting designs for this project in the past.

After some internal strategy work, we have decided to retain our initial corporate identity, Valtry Media.

If you have submitted a design for the original brief and are available, please re-work your best prior design to reflect the color scheme in the newly uploaded logo.

Target Market(s)

This site is aimed primarily at young professionals who buy digital media on behalf of large advertisers.

Industry/Entity Type

Media

Requirements
Must have
• modern white space
Should not have
• no Flash outside of slider

```html
<!DOCTYPE html>
<html lang="en">
<head>
<meta charset="utf-8">
<title>Valtry Media — Online Ad Network</title>
<link rel="stylesheet" href="https://fonts.googleapis.com/css2?family=Montserrat:ital,wght@0,400;0,500;0,600;0,700;1,400;1,600&family=Roboto+Condensed:wght@300;400;700&family=Arimo:wght@400;700&display=swap">
<style>
  :root {
    --red: #b8182a;
    --red-bright: #e0101a;
    --red-deep: #3a0006;
    --ink: #1f1f1f;
    --text: #3a3a3a;
    --lime: #d4dc2a;
    --lime-light: #eef25a;
    --panel: #f5f5f5;
    --panel-light: #fafafa;
    --rule: #8a8a8a;
    --white: #ffffff;
  }
  * { margin: 0; padding: 0; box-sizing: border-box; }
  html, body { width: 1200px; height: 1050px; overflow: hidden; background: var(--white); }
  body { position: relative; font-family: "Arimo", Arial, sans-serif; color: var(--text); }

  .site-header { position: absolute; left: 0; top: 0; width: 1200px; height: 101px; }
  .brand { position: absolute; left: 150px; top: 22px; display: flex; align-items: center; gap: 10px;
    font-family: "Montserrat", sans-serif; font-weight: 500; font-size: 38px; color: var(--ink); letter-spacing: -0.5px; }
  .brand-mark { width: 22px; height: 22px; background: var(--lime); }
  .tagline { position: absolute; right: 119px; top: 11px; font-family: "Montserrat", sans-serif; font-weight: 600;
    font-size: 12px; letter-spacing: 0.4px; color: var(--red); }
  .main-nav { position: absolute; right: 118px; top: 63px; display: flex; }
  .main-nav a { display: block; height: 28px; line-height: 28px; padding: 0 14px; font-family: "Montserrat", sans-serif;
    font-weight: 600; font-size: 12.5px; letter-spacing: 0.5px; color: var(--ink); text-decoration: none;
    border-left: 1px solid #444; }
  .main-nav a:first-child { border-left: none; }
  .main-nav a:nth-child(2) { border-left-color: var(--red); }
  .main-nav a:last-child { padding-right: 0; }

  .hero { position: absolute; left: 0; top: 101px; width: 1200px; height: 429px;
    background: radial-gradient(ellipse 900px 420px at 560px 0, var(--red-bright) 0%, #b8000c 45%, #5a0008 80%, var(--red-deep) 100%); }
  .slide { position: absolute; left: 123px; top: 34px; width: 960px; height: 351px; overflow: hidden;
    background: linear-gradient(135deg, #ffffff 0%, #e7e9ec 60%, #dcdfe3 100%); box-shadow: 0 6px 12px rgba(0,0,0,0.55); }
  .slide-photo { position: absolute; left: 500px; top: 0; width: 370px; height: 351px;
    background: radial-gradient(ellipse at 55% 45%, #c99478 0%, #7a4a34 45%, #3a2218 75%, #e6e8ec 100%); }
  .slide-title { position: absolute; left: 105px; top: 120px; font-family: "Montserrat", sans-serif; font-weight: 700;
    font-size: 41px; color: var(--red); letter-spacing: 0.5px; line-height: 1; }
  .slide-sub { position: absolute; left: 106px; top: 164px; font-family: "Montserrat", sans-serif; font-weight: 500;
    font-size: 21px; line-height: 25px; letter-spacing: 0.8px; color: var(--ink); }
  .slide-arrow { position: absolute; top: 158px; width: 30px; height: 52px; }
  .slide-arrow.prev { left: 20px; }
  .slide-arrow.next { right: 16px; }
  .slide-dots { position: absolute; left: 526px; top: 400px; display: flex; gap: 13px; }
  .slide-dots span { width: 15px; height: 15px; border-radius: 50%; background: var(--white); }
  .slide-dots span.active { background: var(--lime); }

  .reach { position: absolute; left: 0; top: 552px; width: 1200px; height: 30px; }
  .reach-title { position: absolute; left: 0; width: 1146px; text-align: center; font-family: "Montserrat", sans-serif;
    font-size: 23px; letter-spacing: 0.6px; color: var(--ink); }
  .reach-title em { font-style: italic; }
  .reach-title strong { font-style: italic; font-weight: 600; }
  .reach-title .accent { color: var(--red); font-weight: 500; }
  .reach-arrow { position: absolute; top: 0; font-family: "Montserrat", sans-serif; font-weight: 700; font-size: 28px; color: var(--red-bright); }
  .reach-arrow.prev { left: 172px; top: 4px; }
  .reach-arrow.next { left: 1018px; top: -4px; }

  .content { position: absolute; left: 118px; top: 600px; width: 960px; height: 375px; background: var(--panel);
    box-shadow: 0 -4px 8px -4px rgba(0,0,0,0.25), 0 10px 12px -6px rgba(0,0,0,0.3); }
  .content::before { content: ""; position: absolute; left: 0; top: 82px; width: 960px; height: 293px; background: var(--panel-light); }

  .about { position: absolute; left: 0; top: 0; width: 610px; height: 375px; }
  .about-heading { position: absolute; left: 6px; top: 36px; display: flex; align-items: center; gap: 10px;
    font-family: "Roboto Condensed", sans-serif; font-weight: 300; font-size: 25px; color: var(--ink); letter-spacing: 0.3px; }
  .about-heading strong { font-weight: 400; }
  .about-heading .mark { width: 24px; height: 24px; background: var(--lime); }
  .about-lead { position: absolute; left: 5px; top: 78px; width: 560px; font-size: 17.5px; line-height: 24px; color: var(--red); }
  .about-body { position: absolute; left: 4px; top: 135px; width: 550px; font-size: 14px; line-height: 24px; color: var(--text); }
  .about-rule { position: absolute; left: 4px; top: 305px; width: 577px; height: 1px; background: var(--rule); }
  .about-links { position: absolute; left: 2px; top: 324px; display: flex; gap: 0; }
  .about-links a { display: flex; align-items: center; gap: 6px; font-family: "Montserrat", sans-serif; font-weight: 500;
    font-size: 13px; letter-spacing: 0.5px; color: var(--ink); text-decoration: none; }
  .about-links a + a { margin-left: 22px; }
  .about-links svg { width: 12px; height: 12px; }

  .news { position: absolute; left: 610px; top: 0; width: 350px; height: 375px; box-shadow: -6px 0 8px -6px rgba(0,0,0,0.18); }
  .news-tab { position: absolute; left: 2px; top: 28px; width: 238px; height: 39px; padding-left: 30px;
    background: linear-gradient(90deg, var(--lime-light) 0%, var(--lime) 100%); box-shadow: 2px 3px 4px rgba(0,0,0,0.35);
    font-family: "Roboto Condensed", sans-serif; font-size: 24px; line-height: 39px; color: var(--red); letter-spacing: 0.3px; }
  .news-list { position: absolute; left: 39px; top: 85px; width: 295px; list-style: none; }
  .news-list li { margin-bottom: 16px; font-size: 12px; line-height: 16px; color: var(--text); }
  .news-list time { display: block; font-weight: 700; font-size: 12px; letter-spacing: 0.3px; color: var(--red); }

  .site-footer { position: absolute; left: 0; top: 1002px; width: 1232px; text-align: center; font-size: 12px; color: var(--ink); }
</style>
</head>
<body>
  <header class="site-header">
    <div class="brand"><span class="brand-mark"></span>Valtry Media</div>
    <p class="tagline">COMPANY TAGLINE GOES HERE</p>
    <nav class="main-nav">
      <a href="#">BEAUTY</a>
      <a href="#">COOKING</a>
      <a href="#">PARENTING</a>
      <a href="#">ENTERTAINMENT</a>
      <a href="#">VIDEO</a>
      <a href="#">CPC</a>
    </nav>
  </header>

  <section class="hero">
    <div class="slide">
      <div class="slide-photo" role="img" aria-label="Portrait photo of a woman with yellow flowers in her hair"></div>
      <h2 class="slide-title">BEAUTY</h2>
      <p class="slide-sub">SITE SPECIFIC CAMPAIGNS<br>AT RON PRICES</p>
      <svg class="slide-arrow prev" viewBox="0 0 30 52" aria-label="Previous slide"><path d="M24 2 L4 26 L24 50 L28 50 L12 26 L28 2 Z" fill="#1a1a1a"/></svg>
      <svg class="slide-arrow next" viewBox="0 0 30 52" aria-label="Next slide"><path d="M6 2 L26 26 L6 50 L2 50 L18 26 L2 2 Z" fill="#1a1a1a"/></svg>
    </div>
    <div class="slide-dots"><span class="active"></span><span></span><span></span><span></span><span></span><span></span></div>
  </section>

  <section class="reach">
    <span class="reach-arrow prev">«</span>
    <h2 class="reach-title"><em>15 </em><strong>MILLION</strong> <span class="accent">CANADIANS</span></h2>
    <span class="reach-arrow next">»</span>
  </section>

  <main class="content">
    <section class="about">
      <h2 class="about-heading"><span class="mark"></span><span>ABOUT <strong>VALTRY MEDIA</strong></span></h2>
      <p class="about-lead">Lorem ipsum dolor sit amet, consectetur adipiscing elit. Mauris dignissim nulla pharetra risus iaculis at consequat turpis vulputate.</p>
      <p class="about-body">Sed scelerisque magna ut quam scelerisque dictum. Morbi purus quam, sodales id vehicula non, ultricies vitae justo. Vivamus sed augue ut elit dapibus adipiscing vel in elit. Mauris adipiscing, elit a laoreet eleifend, orci lacus condimentum enim, vitae venenatis enim velit ac dolor. Nullam augue mauris, tincidunt et bibendum nec, consequat ut dui. Sed id ante in purus vulputate adipiscing ac non justo. Nulla libero sem, venenatis in fringilla pulvinar, ornare ac diam.</p>
      <div class="about-rule"></div>
      <nav class="about-links">
        <a href="#">ABOUT US <svg viewBox="0 0 12 12"><path d="M1 6 H10 M6 2 L10 6 L6 10" stroke="#c8102e" stroke-width="2" fill="none"/></svg></a>
        <a href="#">CONTACT US <svg viewBox="0 0 12 12"><path d="M1 6 H10 M6 2 L10 6 L6 10" stroke="#c8102e" stroke-width="2" fill="none"/></svg></a>
        <a href="#">MANAGEMENT TEAM <svg viewBox="0 0 12 12"><path d="M1 6 H10 M6 2 L10 6 L6 10" stroke="#c8102e" stroke-width="2" fill="none"/></svg></a>
        <a href="#">NEWS <svg viewBox="0 0 12 12"><path d="M1 6 H10 M6 2 L10 6 L6 10" stroke="#c8102e" stroke-width="2" fill="none"/></svg></a>
        <a href="#">CAREERS <svg viewBox="0 0 12 12"><path d="M1 6 H10 M6 2 L10 6 L6 10" stroke="#c8102e" stroke-width="2" fill="none"/></svg></a>
      </nav>
    </section>

    <aside class="news">
      <h2 class="news-tab">VALTRY NEWS</h2>
      <ul class="news-list">
        <li><time>JANUARY 15, 2011</time>Valtry Media&nbsp; unveils new web site design and digital strategy</li>
        <li><time>DECEMBER 22, 2010</time>Valtry Media featured in Founderwire.com as one of the fastest grown online ad agencies.</li>
        <li><time>NOVEMBER 15, 2010</time>As RTB Goes Mainstream, Display Services Try To Pull Publishers Along</li>
        <li><time>NOVEMBER 9, 2010</time>Morbi purus quam, sodales id vehicula non, ultricies vitae justo</li>
      </ul>
    </aside>
  </main>

  <footer class="site-footer">Copyright 2011 Valtry Media. All Rights Reserved</footer>
</body>
</html>
```